Business Management System Providor Needs Upscale Business Card Design

We provide an online Claims Management System to the Insurance Industry called Meridell Casework Suite. Although our core offering is claims management, our system provides full business management features including reporting, invoicing, business trend analysis, etc..
We have a worldwide client base and our system has become known for its reliability, rich feature set, and intuitive design. This being the case we would like our cards to maintain a high level of professionalism. We have a tendency to lean toward a corporate look and feel and we would like to maintain that image.
Current Site: www.meridellcaseworksuite.example
Target Market(s)
Big Business, Insurance Professionals, Corporate Organizations
Industry/Entity Type
Business Management
Look and feel
Each slider illustrates characteristics of the customer's brand and the style your logo design should communicate.

```html
<!DOCTYPE html>
<html lang="en">
<head>
<meta charset="utf-8">
<title>Meridell Casework Suite – Business Card</title>
<link rel="stylesheet" href="https://fonts.googleapis.com/css2?family=Jura:wght@500;600;700&display=swap">
<style>
  :root {
    --page-bg: #e9eaec;
    --card-bg: #f7f7f8;
    --brand-blue: #2e4f86;
    --band-blue: #3a5d97;
    --band-light: #5a7bb2;
    --swoosh-grey: #c9cbcf;
    --ink: #1e1e22;
    --ink-soft: #333338;
    --white: #ffffff;
  }
  * { box-sizing: border-box; margin: 0; padding: 0; }
  html, body {
    width: 1200px; height: 900px; overflow: hidden;
    background: var(--page-bg);
    font-family: "Jura", sans-serif;
  }
  .card {
    position: absolute; left: 150px; top: 190px;
    width: 900px; height: 520px;
    background: var(--card-bg);
    border-radius: 46px;
    overflow: hidden;
    box-shadow: 0 10px 30px rgba(0,0,0,0.12);
  }
  .card__swoosh { position: absolute; inset: 0; width: 100%; height: 100%; }
  .brand {
    position: absolute; left: 80px; top: 200px;
    display: flex; align-items: center; gap: 18px;
  }
  .brand__square {
    width: 78px; height: 78px; border-radius: 10px;
    background: var(--brand-blue);
  }
  .brand__name {
    color: var(--brand-blue);
    font-weight: 700; font-size: 30px; line-height: 1.02;
  }
  .contact {
    position: absolute; left: 560px; top: 48px;
    color: var(--ink);
  }
  .contact__name { font-size: 30px; font-weight: 600; letter-spacing: 0.5px; }
  .contact__role { font-size: 18px; font-weight: 600; margin-top: 2px; }
  .contact__address { font-size: 17px; font-weight: 600; margin-top: 26px; line-height: 1.3; }
  .contact__list { list-style: none; margin-top: 30px; margin-left: 40px; }
  .contact__item {
    display: flex; align-items: center; gap: 10px;
    font-size: 14px; font-weight: 600; color: var(--ink-soft);
    height: 25px;
  }
  .contact__icon { width: 15px; height: 15px; flex: none; }
  .band-url {
    position: absolute; left: 430px; top: 438px;
    transform: rotate(-9deg);
    color: var(--white);
    font-size: 19px; font-weight: 600; letter-spacing: 3px;
  }
</style>
</head>
<body>
  <div class="card">
    <svg class="card__swoosh" viewBox="0 0 900 520" aria-hidden="true">
      <defs>
        <linearGradient id="bandGrad" x1="0" y1="0" x2="1" y2="0">
          <stop offset="0" stop-color="var(--brand-blue)"/>
          <stop offset="0.6" stop-color="var(--band-light)"/>
          <stop offset="1" stop-color="var(--band-blue)"/>
        </linearGradient>
      </defs>
      <path class="swoosh-grey" d="M0 510 C 300 470, 600 380, 900 268 L 900 300 C 600 400, 300 490, 0 520 Z" fill="var(--swoosh-grey)"/>
      <path class="swoosh-band" d="M0 520 C 300 495, 600 410, 900 292 L 900 520 Z" fill="url(#bandGrad)"/>
    </svg>

    <div class="brand">
      <span class="brand__square"></span>
      <span class="brand__name">Meridell<br>Casework<br>Suite</span>
    </div>

    <div class="contact">
      <p class="contact__name">Tobin Hale</p>
      <p class="contact__role">General Manager</p>
      <p class="contact__address">041,12th floor,Court<br>Ashfield Road NRT</p>
      <ul class="contact__list">
        <li class="contact__item">
          <svg class="contact__icon" viewBox="0 0 16 16"><circle cx="8" cy="8" r="8" fill="var(--ink)"/><path d="M5 4.5l1.6-.3.8 2-1 .8a5 5 0 0 0 2.6 2.6l.8-1 2 .8-.3 1.6c-3.5.3-7-3.2-6.5-6.5z" fill="var(--white)"/></svg>
          020 481 7356
        </li>
        <li class="contact__item">
          <svg class="contact__icon" viewBox="0 0 16 16"><circle cx="8" cy="8" r="8" fill="var(--ink)"/><rect x="5.5" y="3.5" width="5" height="9" rx="1" fill="var(--white)"/></svg>
          020 481 7356
        </li>
        <li class="contact__item">
          <svg class="contact__icon" viewBox="0 0 16 16"><circle cx="8" cy="8" r="8" fill="var(--ink)"/><rect x="4" y="5" width="8" height="6" fill="var(--white)"/><path d="M4 5l4 3 4-3" stroke="var(--ink)" fill="none"/></svg>
          tobin@meridell.example
        </li>
        <li class="contact__item">
          <svg class="contact__icon" viewBox="0 0 16 16"><circle cx="8" cy="8" r="8" fill="var(--ink)"/><circle cx="8" cy="8" r="4.5" stroke="var(--white)" fill="none"/><path d="M3.5 8h9M8 3.5v9" stroke="var(--white)"/></svg>
          www.meridellcaseworksuite.example
        </li>
      </ul>
    </div>

    <p class="band-url">www.meridellcaseworksuite.example</p>
  </div>
</body>
</html>
```